Business Cards and Stationery Set
Curavend Healthcare
Professional
Teodor Lisk, MD
Managing Partner
4318 West Birch Lane, Suite 207-3
Fresno, CA 93520 USA
tlisk@curavendcare.example
www.curavendcare.example

```html
<!DOCTYPE html>
<html lang="en">
<head>
<meta charset="utf-8">
<title>Curavend Healthcare – Business Card</title>
<link rel="stylesheet" href="https://fonts.googleapis.com/css2?family=Open+Sans:wght@400;600;700&display=swap">
<style>
  :root {
    --bg: #e9e4df;
    --card-white: #ffffff;
    --brand-red: #c0161c;
    --deep-red: #6e0d12;
    --mid-red: #9a141a;
    --ink: #2a2a2a;
    --muted: #555555;
    --shadow: rgba(0,0,0,0.25);
  }
  * { margin: 0; padding: 0; box-sizing: border-box; }
  html, body {
    width: 1200px; height: 859px; overflow: hidden;
    background: var(--bg);
    font-family: "Open Sans", Arial, sans-serif;
  }
  .canvas { position: relative; width: 1200px; height: 859px; }

  .card {
    position: absolute;
    width: 540px; height: 306px;
    box-shadow: 0 6px 18px var(--shadow);
    overflow: hidden;
  }

  /* Front */
  .card-front { left: 110px; top: 60px; background: var(--card-white); }
  .brand {
    position: absolute; left: 0; right: 0; top: 38px;
    display: flex; align-items: center; justify-content: center; gap: 16px;
  }
  .brand-dot {
    width: 58px; height: 58px; border-radius: 50%;
    background: var(--brand-red);
  }
  .brand-name {
    color: var(--brand-red); font-weight: 600; font-size: 26px; line-height: 1.15;
  }
  .person { position: absolute; left: 0; right: 0; top: 134px; text-align: center; }
  .person-name { color: var(--brand-red); font-weight: 700; font-size: 19px; }
  .person-title { color: var(--ink); font-size: 11px; margin-top: 1px; }
  .contact {
    position: absolute; left: 0; right: 0; top: 190px;
    text-align: center; color: var(--muted); font-size: 9.5px; line-height: 1.45;
  }
  .front-band { position: absolute; left: 0; bottom: 0; width: 540px; height: 72px; }
  .front-url {
    position: absolute; left: 0; right: 0; bottom: 12px;
    text-align: center; color: #fff; font-size: 11px; font-weight: 600;
  }

  /* Back */
  .card-back {
    left: 560px; top: 470px;
    background: radial-gradient(ellipse at 50% 40%, var(--brand-red) 0%, var(--mid-red) 40%, var(--deep-red) 100%);
  }
  .back-brand {
    position: absolute; left: 0; right: 0; top: 92px;
    display: flex; align-items: center; justify-content: center; gap: 14px;
  }
  .back-dot { width: 64px; height: 64px; border-radius: 50%; background: #fff; }
  .back-name { color: #fff; font-weight: 600; font-size: 26px; }
  .back-url {
    position: absolute; left: 0; right: 0; bottom: 62px;
    text-align: center; color: #fff; font-size: 11px; font-weight: 600;
  }
</style>
</head>
<body>
<main class="canvas">
  <section class="card card-front">
    <div class="brand">
      <span class="brand-dot"></span>
      <span class="brand-name">Curavend<br>Healthcare L.L.C.</span>
    </div>
    <div class="person">
      <p class="person-name">Teodor Lisk</p>
      <p class="person-title">Managing Partner</p>
    </div>
    <div class="contact">
      <p>4318 West Birch Lane, Suite 207-3 Fresno, CA 93520 USA</p>
      <p>Phone: +1 559 555 0148 &nbsp;|&nbsp; Cell: +1 248 555 0172</p>
      <p>Email: tlisk@curavendcare.example</p>
    </div>
    <svg class="front-band" viewBox="0 0 540 72" preserveAspectRatio="none" aria-hidden="true">
      <path d="M0 26 Q270 0 540 26 L540 72 L0 72 Z" fill="#1e1e1e"/>
      <path d="M0 32 Q270 8 540 32 L540 72 L0 72 Z" fill="var(--brand-red)"/>
    </svg>
    <p class="front-url">www.curavendcare.example</p>
  </section>

  <section class="card card-back">
    <div class="back-brand">
      <span class="back-dot"></span>
      <span class="back-name">Curavend</span>
    </div>
    <p class="back-url">www.curavendcare.example</p>
  </section>
</main>
</body>
</html>
```